Lantern Advisory Business Cards

We need a new layout for our business cards. We have a logo already. But we might be interested in only using the Lantern portion of the logo. It has been uploaded.

We would like cards that are not overly busy. Clean. Modern. Perhaps a gray color for one side.

On the back, we would like to have the lantern part of the logo and "Step forward, we stand with you!"

Our business provides medics and safety training for corporate clients. Our website is www.lanternadvisoryllc.example.

Industry/Entity Type

Business

Contact Information for Business Card

We want include name, email address, cell phone, main line number, and website URL on the front. Use the following as an example: Marla Tobin, marla@lanternadvisoryllc.example, 402.318.7264 (cell), 402.947.315, and www.lanternadvisoryllc.example.

Font styles to use
Serif
Sans Serif

Requirements
Must have
• All required information. Back side logo with "Take the leap, we will catch you!"
Nice to have
• If possible, we would like to consider creating a card in a non-standard shape. Perhaps, the shape of a lantern. Just interested in understanding the option.

```html
<!DOCTYPE html>
<html lang="en">
<head>
<meta charset="utf-8">
<title>Lantern Advisory Business Cards</title>
<link rel="stylesheet" href="https://fonts.googleapis.com/css2?family=Open+Sans:wght@400;600;700&display=swap">
<style>
  :root {
    --backdrop: #e6e6e4;
    --card-white: #f8f8f7;
    --brand-blue: #0b7fb4;
    --accent-blue: #1b55a6;
    --ink: #1d1d1f;
    --muted: #6a6a6e;
    --white: #ffffff;
  }
  * { box-sizing: border-box; margin: 0; padding: 0; }
  html, body {
    width: 1200px; height: 900px; overflow: hidden;
    background: var(--backdrop);
  }
  .stage {
    width: 1200px; height: 900px;
    display: flex; align-items: center; justify-content: center; gap: 60px;
  }
  .card {
    position: relative;
    width: 520px; height: 300px;
    box-shadow: 0 6px 20px rgba(0,0,0,0.18);
  }
  /* Front */
  .card--front { background: var(--card-white); }
  .brand {
    position: absolute; left: 34px; top: 44px;
    display: flex; align-items: center; gap: 10px;
  }
  .brand__dot {
    width: 14px; height: 14px; border-radius: 50%;
    background: var(--accent-blue);
  }
  .brand__text { display: flex; flex-direction: column; }
  .brand__name {
    font-family: "Open Sans", sans-serif; font-weight: 600;
    font-size: 26px; color: var(--ink); line-height: 1.1;
  }
  .brand__tagline {
    font-family: "Open Sans", sans-serif; font-size: 11px;
    color: var(--muted); margin-top: 4px;
  }
  .holder {
    position: absolute; right: 30px; top: 118px;
    font-family: "Open Sans", sans-serif; font-weight: 700;
    font-size: 18px; color: var(--accent-blue);
  }
  .rule {
    position: absolute; left: 0; right: 0; top: 148px;
    height: 1.5px; background: var(--accent-blue);
  }
  .contact {
    position: absolute; right: 30px; top: 166px;
    list-style: none;
    font-family: "Open Sans", sans-serif; font-size: 14.5px; color: var(--ink);
  }
  .contact__item {
    display: flex; justify-content: flex-end; align-items: center; gap: 9px;
    line-height: 26px;
  }
  .contact__icon { width: 13px; height: 13px; flex: none; }
  /* Back */
  .card--back { background: var(--brand-blue); }
  .back-mark {
    position: absolute; left: 0; right: 0; top: 92px;
    display: flex; justify-content: center; align-items: center; gap: 12px;
  }
  .back-mark__dot {
    width: 18px; height: 18px; border-radius: 50%; background: var(--white);
  }
  .back-mark__name {
    font-family: "Open Sans", sans-serif; font-weight: 600;
    font-size: 32px; color: var(--white);
  }
  .motto {
    position: absolute; left: 0; right: 0; top: 226px;
    display: flex; align-items: center; gap: 12px;
  }
  .motto__line { flex: 1; height: 1.5px; background: var(--white); }
  .motto__text {
    font-family: "Open Sans", sans-serif; font-weight: 600;
    font-size: 13.5px; color: var(--white); text-transform: uppercase;
    white-space: nowrap;
  }
</style>
</head>
<body>
<main class="stage">
  <section class="card card--front" aria-label="Card front">
    <div class="brand">
      <span class="brand__dot"></span>
      <div class="brand__text">
        <span class="brand__name">Lantern Advisory</span>
        <span class="brand__tagline">Ready when it counts</span>
      </div>
    </div>
    <p class="holder">Marla Tobin</p>
    <div class="rule"></div>
    <ul class="contact">
      <li class="contact__item">402.318.7264
        <svg class="contact__icon" viewBox="0 0 14 14" aria-hidden="true"><rect x="2.5" y="1" width="9" height="12" rx="1.5" fill="none" stroke="#1b55a6" stroke-width="1.6"/><circle cx="7" cy="10.8" r="0.9" fill="#1b55a6"/></svg>
      </li>
      <li class="contact__item">402.947.315
        <svg class="contact__icon" viewBox="0 0 14 14" aria-hidden="true"><path d="M3.2 1.2 5.4 3.6 4.3 5.2c.9 1.9 2.5 3.5 4.4 4.4l1.6-1.1 2.4 2.2-1.3 2c-5.6-.4-10-4.8-10.4-10.4z" fill="#1b55a6"/></svg>
      </li>
      <li class="contact__item">marla@lanternadvisoryllc.example
        <svg class="contact__icon" viewBox="0 0 14 14" aria-hidden="true"><rect x="1" y="3" width="12" height="8.5" fill="#1b55a6"/><path d="M1.5 3.5 7 8l5.5-4.5" fill="none" stroke="#f8f8f7" stroke-width="1.1"/></svg>
      </li>
      <li class="contact__item">www.lanternadvisoryllc.example
        <svg class="contact__icon" viewBox="0 0 14 14" aria-hidden="true"><circle cx="7" cy="7" r="6" fill="#1b55a6"/><path d="M1 7h12M7 1c-2.4 3-2.4 9 0 12M7 1c2.4 3 2.4 9 0 12" fill="none" stroke="#f8f8f7" stroke-width="0.9"/></svg>
      </li>
    </ul>
  </section>

  <section class="card card--back" aria-label="Card back">
    <div class="back-mark">
      <span class="back-mark__dot"></span>
      <span class="back-mark__name">Lantern Advisory</span>
    </div>
    <div class="motto">
      <span class="motto__line"></span>
      <span class="motto__text">Step forward, we stand with you!</span>
      <span class="motto__line"></span>
    </div>
  </section>
</main>
</body>
</html>
```